New Product Launch! Nothing on the market like it.

Incorporate the tag line ' New Day | New Year | New Corvane. Progress starts with Lumetta'.
2 infographs 1) All Weather2) UV Resistant- Position both topics as 'what that means'. For example, we can make this claim because we did the testing. A lot of our competitors make these claims and should not, nor do they perform anywhere close to Lumetta.
For the All Weather- Use graphics for each stage of temperature testing that look weather related; snow flake, oven, water, freezer, thermometer. I also want to communicate that after all that testing the bond strength of Lumetta stayed intact.
UV resistance, similar- competitors make UV claims, NONE come close to our performance nor have any products been subjected to these kinds of tests. I want to include that Lumetta Resists cracking, yellowing, and delamination even after years of continuous UV bombardment. This exceptional performance ensures long-term aesthetic and functional reliability in applications, and sustained UV exposure without compromising bond performance or appearance (or something similar). Would also like to include the tag line, 'Progress starts with Lumetta'.
Please use the attached deck to coordinate the All Weather and UV Resistance Claims to the testing.
All Weather- Engineered for both indoor and outdoor applications without compromising reliability under any conditions. Tested to ASTM D1183-03, subjected to multiple rounds of 230 hours of testing. Ambient Cure-64 hours | 71°C oven-48 hours | 23°C submerged in Water-48 hours | -10°C freezer- 8 hours | 38.5°C oven- 64 hours. The bond strength was barely affected.
High UV Resistance- Maintains color and integrity in sunlight where standard adhesives discolor or degrade over time. Resists cracking, yellowing, and delamination even after years of continuous use and exposure. 10X Less Yellowing- exposed to 100 hrs of UV in 20hr increments using a UVA 340 0- simulating direct noon sun, in accordance to ISO 4892-3- which is equivalent to 1 year under the florida sun. Lumetta measures a 1.5∆E while competitors read 11∆E

Target Market(s)

Fabricators (indoor/outdoor countertop) and Distributors

Industry/Entity Type

Subcontractor and Distributor

Colors
EE7325
F08F49
F5BC92
FAE3D3
FDF4ED

Requirements
Must have
• 2 infographs

```html
<!DOCTYPE html>
<html lang="en">
<head>
<meta charset="utf-8">
<title>Corvane Adhesives – All Weather &amp; High UV Resistance Infographics</title>
<link href="https://fonts.googleapis.com/css2?family=Oswald:wght@400;500;600;700&family=Montserrat:wght@500;600;700&family=Questrial&display=swap" rel="stylesheet">
<style>
  :root{
    --orange:#EE7325;
    --orange-light:#F08F49;
    --peach:#F5BC92;
    --blush:#FAE3D3;
    --cream:#FDF4ED;
    --ink:#1d1d1b;
    --stage:#EBCBC2;
    --white:#ffffff;
  }
  *{box-sizing:border-box;margin:0;padding:0}
  html,body{width:1200px;height:600px;overflow:hidden;background:var(--stage)}
  .stage{position:relative;width:1200px;height:600px}
  .card{position:absolute;top:117px;width:474px;height:366px;background:var(--white);overflow:hidden}
  .card--weather{left:63px}
  .card--uv{left:663px}

  .deco{position:absolute;pointer-events:none}
  .deco--top{right:0;top:0;width:230px;height:140px;background:radial-gradient(ellipse at 70% 20%,var(--blush) 0%,var(--cream) 45%,rgba(253,244,237,0) 75%);opacity:.8}
  .deco--bottom{left:0;bottom:22px;width:170px;height:110px;background:radial-gradient(ellipse at 20% 80%,var(--blush) 0%,var(--cream) 45%,rgba(253,244,237,0) 75%);opacity:.8}

  .headline{position:absolute;left:27px;top:25px;right:25px;display:flex;align-items:center;gap:12px;font-family:'Montserrat',sans-serif;font-weight:700;font-size:17px;letter-spacing:.2px;color:var(--ink);white-space:nowrap}
  .headline .accent{color:var(--orange)}
  .headline-rule{flex:1;height:3px}
  .card--weather .headline-rule{background:linear-gradient(90deg,var(--orange) 55%,#5a2a10 100%)}
  .card--uv .headline-rule{background:linear-gradient(90deg,var(--ink) 55%,var(--orange) 100%)}

  .intro{position:absolute;left:27px;top:51px;font-family:'Oswald',sans-serif;font-weight:500;font-size:10.4px;line-height:13.8px;color:var(--ink);text-transform:uppercase;letter-spacing:-.1px}
  .intro .accent{color:var(--orange)}

  .brand{position:absolute;right:26px;top:56px;display:flex;align-items:center;gap:6px}
  .brand-name{font-family:'Oswald',sans-serif;font-weight:600;font-size:32px;line-height:1;color:var(--ink);letter-spacing:-.3px}
  .brand-dot{width:7px;height:7px;border-radius:50%;background:var(--orange)}

  .claim-bar{position:absolute;left:27px;right:25px;top:124px;height:15px;display:flex;font-family:'Montserrat',sans-serif;font-weight:600;font-size:10.4px;color:var(--white);white-space:nowrap}
  .claim-bar .tag{display:flex;align-items:center;padding:0 5px}
  .claim-bar .text{flex:1;display:flex;align-items:center;padding:0 10px}
  .card--weather .tag{background:var(--ink);width:146px}
  .card--weather .text{background:var(--orange)}
  .card--uv .tag{background:var(--orange);width:48px;justify-content:center;font-family:'Oswald',sans-serif;font-size:10.4px;letter-spacing:.3px}
  .card--uv .text{background:var(--ink);font-size:8.6px;font-weight:500;padding-left:6px}
  .card--uv .text em{font-style:italic}

  .tests{position:absolute;left:27px;top:158px;display:flex;gap:20px}
  .test{position:relative;width:90px;height:108px;border:2px solid var(--orange);background:linear-gradient(135deg,var(--white) 55%,var(--blush) 55%)}
  .test--cold{border-color:var(--ink)}
  .test-therm{position:absolute;left:6px;top:3px;width:10px;height:28px}
  .test-icon{position:absolute;left:50%;top:-10px;width:46px;height:46px;margin-left:-20px;border-radius:50%;background:var(--orange);display:flex;align-items:center;justify-content:center}
  .test--cold .test-icon{background:var(--ink)}
  .test-temp{position:absolute;left:0;right:0;top:39px;text-align:center;font-family:'Oswald',sans-serif;font-weight:700;font-size:29px;line-height:1;color:var(--ink);letter-spacing:-.5px}
  .test-medium{position:absolute;left:0;right:0;top:72px;text-align:center;font-family:'Oswald',sans-serif;font-weight:500;font-size:9.6px;color:var(--ink);white-space:nowrap}
  .test-duration{position:absolute;left:0;right:0;bottom:0;height:19px;background:var(--orange);color:var(--white);font-family:'Montserrat',sans-serif;font-weight:600;font-size:11.5px;display:flex;align-items:center;justify-content:center}
  .test--cold .test-duration{background:var(--ink)}
  .test-duration::after{content:"";position:absolute;right:-2px;bottom:-2px;border-style:solid;border-width:0 0 9px 9px;border-color:transparent transparent var(--ink) transparent}
  .test--cold .test-duration::after{border-color:transparent transparent var(--orange) transparent}

  .result{position:absolute;left:0;right:0;top:278px;text-align:center;font-family:'Questrial',sans-serif;font-size:10.6px;color:var(--ink)}

  .tagline{position:absolute;left:0;right:0;top:318px;text-align:center;font-family:'Questrial',sans-serif;font-weight:400;font-size:15px;letter-spacing:2.6px;color:var(--ink);text-transform:uppercase;-webkit-text-stroke:.4px var(--ink)}
  .tagline .accent{color:var(--orange);-webkit-text-stroke:.4px var(--orange)}

  .footer-band{position:absolute;left:0;right:0;bottom:0;height:23px}
  .card--weather .footer-band{background:linear-gradient(180deg,var(--orange-light),var(--orange))}
  .card--uv .footer-band{background:linear-gradient(180deg,#3a3a38,var(--ink))}
  .footer-corner{position:absolute;right:0;bottom:0;border-style:solid;border-width:0 0 23px 23px}
  .card--weather .footer-corner{border-color:transparent transparent var(--ink) transparent}
  .card--uv .footer-corner{border-color:transparent transparent var(--orange) transparent}

  /* UV card */
  .delta-table{position:absolute;left:27px;top:158px;display:grid;grid-template-columns:52px 73px;column-gap:3px;row-gap:4px}
  .delta-head{height:21px;display:flex;align-items:center;justify-content:center;font-family:'Oswald',sans-serif;font-weight:500;font-size:8.8px;white-space:nowrap}
  .delta-head--range{background:var(--ink);color:var(--white)}
  .delta-head--guide{background:var(--orange);color:var(--white);flex-direction:column;line-height:1}
  .delta-head--guide small{font-size:3.8px;letter-spacing:.6px;margin-top:1px}
  .delta-range{height:25px;background:var(--ink);color:var(--white);font-family:'Montserrat',sans-serif;font-weight:600;font-size:10.6px;display:flex;align-items:center;justify-content:center}
  .delta-note{height:25px;background:var(--orange);color:var(--ink);font-family:'Montserrat',sans-serif;font-weight:500;font-size:4.8px;line-height:1.2;text-align:center;display:flex;align-items:center;justify-content:center;padding:0 2px;white-space:nowrap}

  .exposure{position:absolute;left:186px;top:160px;width:100px;text-align:center;font-family:'Montserrat',sans-serif;font-weight:700;color:var(--ink);line-height:1;white-space:nowrap}
  .exposure .lead{font-size:11.4px;letter-spacing:.6px}
  .exposure .figure{margin:3px 0 0;background:var(--orange);color:var(--white);padding:2px 0 3px;box-shadow:inset 0 0 0 2px var(--orange-light)}
  .exposure .figure b{display:block;font-size:38px;letter-spacing:-1px;line-height:1}
  .exposure .figure span{display:block;font-size:11.6px;letter-spacing:2.4px}
  .exposure .l1{font-size:16px;margin-top:5px;letter-spacing:.4px}
  .exposure .l2{font-size:16px;color:var(--orange);letter-spacing:.4px;margin-top:1px}
  .exposure .l3{font-size:11.8px;color:var(--orange);letter-spacing:.2px;margin-top:2px}
  .exposure .l4{font-family:'Oswald',sans-serif;font-weight:600;font-size:13px;color:var(--orange);margin-top:1px}

  .sunlight{position:absolute;left:313px;top:158px;width:136px;font-family:'Montserrat',sans-serif;font-weight:700;color:var(--ink);line-height:1;text-align:center;white-space:nowrap}
  .sunlight .bar{background:var(--ink);color:var(--white);font-size:9.6px;letter-spacing:.8px;padding:2px 0}
  .sunlight .noon{font-family:'Oswald',sans-serif;font-weight:700;font-size:34px;color:var(--orange);line-height:1.05;letter-spacing:-.5px;margin-top:1px}
  .sunlight .acc{font-size:12.4px;letter-spacing:.2px;margin-top:1px}
  .sunlight .iso{background:var(--orange);color:var(--white);font-size:12.6px;letter-spacing:1.2px;padding:2px 0;margin-top:3px}
  .sunlight .eq{font-size:10px;margin-top:6px}
  .sunlight .eq2{font-size:12.4px;margin-top:3px}
  .sunlight .eq2 .accent{color:var(--orange)}
  .sunlight .eq3{font-size:12.4px;margin-top:3px}
</style>
</head>
<body>
<main class="stage">

  <!-- All Weather infographic -->
  <section class="card card--weather" aria-label="All Weather infographic">
    <div class="deco deco--top" role="img" aria-label="Faint geometric arcs and circles pattern"></div>
    <div class="deco deco--bottom" role="img" aria-label="Faint geometric arcs and circles pattern"></div>

    <h2 class="headline"><span>ALL <span class="accent">WEATHER</span></span><span class="headline-rule"></span></h2>

    <p class="intro">Engineered for both <span class="accent">indoor</span><br><span class="accent">and outdoor</span> applications<br>without compromising reliability<br>under any conditions</p>

    <div class="brand"><span class="brand-name">Corvane Adhesives</span><span class="brand-dot"></span></div>

    <div class="claim-bar"><span class="tag">Tested to ASTM D1183-03</span><span class="text">Subjected to multiple rounds of 230 hours of testing</span></div>

    <div class="tests">
      <article class="test">
        <svg class="test-therm" viewBox="0 0 10 28"><rect x="3" y="1" width="4" height="19" rx="2" fill="none" stroke="#1d1d1b" stroke-width="1"/><rect x="4.3" y="9" width="1.4" height="12" fill="#EE7325"/><circle cx="5" cy="23" r="3.5" fill="#1d1d1b"/><path d="M7.5 5h2M7.5 8h2M7.5 11h2M7.5 14h2" stroke="#1d1d1b" stroke-width=".6"/></svg>
        <div class="test-icon"><svg width="24" height="24" viewBox="0 0 24 24"><rect x="3" y="2" width="18" height="20" rx="2" fill="#fff"/><rect x="5" y="7.5" width="14" height="12" rx="1" fill="#EE7325"/><circle cx="7" cy="4.8" r="1" fill="#EE7325"/><circle cx="10.5" cy="4.8" r="1" fill="#EE7325"/><circle cx="14" cy="4.8" r="1" fill="#EE7325"/><path d="M9 11c-1 1.5 1 2.5 0 4M12 11c-1 1.5 1 2.5 0 4M15 11c-1 1.5 1 2.5 0 4" stroke="#fff" stroke-width="1" fill="none"/></svg></div>
        <div class="test-temp">71°C</div>
        <div class="test-medium">OVEN</div>
        <div class="test-duration">48 HOURS</div>
      </article>
      <article class="test">
        <svg class="test-therm" viewBox="0 0 10 28"><rect x="3" y="1" width="4" height="19" rx="2" fill="none" stroke="#1d1d1b" stroke-width="1"/><rect x="4.3" y="12" width="1.4" height="9" fill="#EE7325"/><circle cx="5" cy="23" r="3.5" fill="#1d1d1b"/><path d="M7.5 5h2M7.5 8h2M7.5 11h2M7.5 14h2" stroke="#1d1d1b" stroke-width=".6"/></svg>
        <div class="test-icon"><svg width="26" height="26" viewBox="0 0 26 26"><path d="M13 2c3 4 4.5 6.5 4.5 8.5a4.5 4.5 0 0 1-9 0C8.5 8.5 10 6 13 2z" fill="#fff"/><path d="M3 16c2.5-2 5-2 7.5 0s5 2 7.5 0 5-2 5 0M3 20c2.5-2 5-2 7.5 0s5 2 7.5 0 5-2 5 0M3 24c2.5-2 5-2 7.5 0s5 2 7.5 0 5-2 5 0" stroke="#fff" stroke-width="1.6" fill="none"/></svg></div>
        <div class="test-temp">23°C</div>
        <div class="test-medium">SUBMERGED IN WATER</div>
        <div class="test-duration">48 HOURS</div>
      </article>
      <article class="test test--cold">
        <svg class="test-therm" viewBox="0 0 10 28"><rect x="3" y="1" width="4" height="19" rx="2" fill="none" stroke="#1d1d1b" stroke-width="1"/><rect x="4.3" y="16" width="1.4" height="5" fill="#EE7325"/><circle cx="5" cy="23" r="3.5" fill="#1d1d1b"/><path d="M7.5 5h2M7.5 8h2M7.5 11h2M7.5 14h2" stroke="#1d1d1b" stroke-width=".6"/></svg>
        <div class="test-icon"><svg width="28" height="24" viewBox="0 0 28 24"><rect x="2" y="4" width="24" height="17" rx="2" fill="#fff"/><rect x="4" y="2" width="20" height="4" rx="1" fill="none" stroke="#fff" stroke-width="1.2"/><circle cx="10" cy="13" r="6" fill="#1d1d1b"/><path d="M10 8v10M5.7 10.5l8.6 5M5.7 15.5l8.6-5" stroke="#fff" stroke-width="1.2"/><rect x="18" y="10" width="6" height="7" rx="1" fill="#1d1d1b"/></svg></div>
        <div class="test-temp">-10°C</div>
        <div class="test-medium">FREEZER</div>
        <div class="test-duration">8 HOURS</div>
      </article>
      <article class="test">
        <svg class="test-therm" viewBox="0 0 10 28"><rect x="3" y="1" width="4" height="19" rx="2" fill="none" stroke="#1d1d1b" stroke-width="1"/><rect x="4.3" y="10" width="1.4" height="11" fill="#EE7325"/><circle cx="5" cy="23" r="3.5" fill="#1d1d1b"/><path d="M7.5 5h2M7.5 8h2M7.5 11h2M7.5 14h2" stroke="#1d1d1b" stroke-width=".6"/></svg>
        <div class="test-icon"><svg width="24" height="24" viewBox="0 0 24 24"><rect x="3" y="2" width="18" height="20" rx="2" fill="#fff"/><rect x="5" y="7.5" width="14" height="12" rx="1" fill="#EE7325"/><circle cx="7" cy="4.8" r="1" fill="#EE7325"/><circle cx="10.5" cy="4.8" r="1" fill="#EE7325"/><circle cx="14" cy="4.8" r="1" fill="#EE7325"/><path d="M9 11c-1 1.5 1 2.5 0 4M12 11c-1 1.5 1 2.5 0 4M15 11c-1 1.5 1 2.5 0 4" stroke="#fff" stroke-width="1" fill="none"/></svg></div>
        <div class="test-temp">38.5°C</div>
        <div class="test-medium">OVEN</div>
        <div class="test-duration">64 HOURS</div>
      </article>
    </div>

    <p class="result">The bond strength was barely affected.</p>

    <p class="tagline">Progress starts with <span class="accent">Lumetta</span></p>

    <div class="footer-band"><span class="footer-corner"></span></div>
  </section>

  <!-- High UV Resistance infographic -->
  <section class="card card--uv" aria-label="High UV Resistance infographic">
    <div class="deco deco--top" role="img" aria-label="Faint geometric arcs and circles pattern"></div>
    <div class="deco deco--bottom" role="img" aria-label="Faint geometric arcs and circles pattern"></div>

    <h2 class="headline"><span><span class="accent">HIGH UV</span> RESISTANCE</span><span class="headline-rule"></span></h2>

    <p class="intro">Maintains color and integrity<br>in sunlight where <span class="accent">standard</span><br><span class="accent">adhesives discolor</span><br>or degrade over time</p>

    <div class="brand"><span class="brand-name">Corvane Adhesives</span><span class="brand-dot"></span></div>

    <div class="claim-bar"><span class="tag">RESISTS</span><span class="text">Cracking, yellowing, and delamination&nbsp;<em>even after years of continuous use and exposure</em></span></div>

    <div class="delta-table">
      <div class="delta-head delta-head--range">GENERAL ΔE</div>
      <div class="delta-head delta-head--guide">PERCEPTION GUIDE<small>[ APPLIES TO YELLOWING ]</small></div>
      <div class="delta-range">1.0 - 2.0</div>
      <div class="delta-note">Slight difference,<br>only obvious to trained<br>eyes under specific lighting<br>Lumetta 1.5ΔE</div>
      <div class="delta-range">2.0 - 3.0</div>
      <div class="delta-note">A visible, acceptable<br>difference in many<br>application</div>
      <div class="delta-range">3.0 - 6.0</div>
      <div class="delta-note">Clearly noticeable,<br>obvious difference.<br>Competition</div>
      <div class="delta-range">&gt; 6.0</div>
      <div class="delta-note">Very obvious,<br>significant difference.<br>Competition</div>
    </div>

    <div class="exposure">
      <div class="lead">EXPOSED TO</div>
      <div class="figure"><b>100</b><span>HOURS</span></div>
      <div class="l1">OF UV IN</div>
      <div class="l2">20 HOUR</div>
      <div class="l3">INCREMENTS</div>
      <div class="l4">USING A UVA 340</div>
    </div>

    <div class="sunlight">
      <div class="bar">SIMULATING DIRECT</div>
      <div class="noon">NOON SUN</div>
      <div class="acc">IN ACCORDANCE</div>
      <div class="iso">TO ISO 4892-3</div>
      <div class="eq">WHICH IS EQUIVALENT</div>
      <div class="eq2">TO <span class="accent">1 YEAR</span> UNDER</div>
      <div class="eq3">THE FLORIDA SUN</div>
    </div>

    <p class="tagline">Progress starts with <span class="accent">Lumetta</span></p>

    <div class="footer-band"><span class="footer-corner"></span></div>
  </section>

</main>
</body>
</html>
```